Flyer für Fußball-Förderverein
Zielgruppe
Wir sind der Fußball-Förderverein des SpVg Halmbeck.
Aufgabenstellung
1. Ziel des Flyers:
Der Flyer soll den Förderverein des SpVg Halmbeck bekannter machen und neue Mitglieder und Sponsoren gewinnen. Er soll darüber informieren, wie der Förderverein den Verein unterstützt und warum eine Mitgliedschaft oder eine Spende wichtig ist.
2. Zielgruppe:
Eltern der Kinder und Jugendlichen, die im SpVg Halmbeck Fußball spielen.
Lokale Unternehmen und potenzielle Sponsoren.
Vereinsmitglieder und Fußballinteressierte in der Region.
3. Hauptbotschaft:
„Unterstütze den SpVg Halmbeck – Gemeinsam für die Zukunft unseres Vereins und der Jugend!“
4. Inhalte:
Über den Förderverein:
Eine kurze Beschreibung des Fördervereins, warum er existiert und was er für den Verein und die Jugend tut.
Mitgliedschaft:
Informationen, wie man Mitglied im Förderverein werden kann. Vorteile und der Beitrag, der benötigt wird.
Spenden:
Möglichkeit der direkten Spende mit einem Hinweis auf steuerliche Vorteile (falls zutreffend). Möglicherweise auch die Angabe eines Spendenkontos.
Beispiele für die Verwendung von Mitteln:
Welche Projekte oder Anschaffungen wurden durch den Förderverein unterstützt (z.B. Trainingsmaterialien, Ausrüstung, Turniere, Jugendfahrten)?
Kontaktinformationen:
Ansprechpartner des Fördervereins mit Telefonnummer, E-Mail-Adresse und eventuell ein Link zur Webseite oder Social-Media-Profilen.
5. Designvorgaben:
Farben und Stil:
Die Vereinsfarben des SpVg Halmbeck sollten im Flyer dominieren (grün-weiß, etc.). Ein modernes, aber sportliches Design, das dynamisch wirkt und die Zielgruppe anspricht.
Logo:
Das Logo des SpVg Halmbeck sollte prominent platziert werden, ebenso das Logo des Fördervereins (falls vorhanden).
Bilder:
Verwendung von Bildern aus dem Vereinsleben, insbesondere von Kindern und Jugendlichen im Spielbetrieb oder bei Vereinsaktivitäten. Falls keine spezifischen Bilder vorhanden sind, können allgemeine Fußballbilde..

```html
<!DOCTYPE html>
<html lang="de">
<head>
<meta charset="utf-8">
<title>Förderverein SpVg Halmbeck – Flyer Vorder- und Rückseite</title>
<link href="https://fonts.googleapis.com/css2?family=Oswald:wght@600&family=Poppins:wght@400;600;700;800&display=swap" rel="stylesheet">
<style>
  :root {
    --green: #1a9a43;
    --green-dark: #0f7a32;
    --white: #ffffff;
    --ink: #1d1d1d;
    --black: #0b0b0b;
    --backdrop: #e4e4e4;
  }
  * { box-sizing: border-box; margin: 0; padding: 0; }
  html, body { width: 889px; height: 1200px; overflow: hidden; background: var(--backdrop); }
  .canvas { position: relative; width: 889px; height: 1200px; background: var(--backdrop); }
  .page-slot { position: absolute; top: 308px; width: 432px; height: 583px; box-shadow: 0 4px 14px rgba(0,0,0,.18); overflow: hidden; }
  .page-slot--front { left: 8px; }
  .page-slot--back { left: 449px; }
  .page { position: absolute; left: 0; top: 0; width: 889px; height: 1200px; transform: scale(0.486); transform-origin: 0 0; font-family: "Poppins", sans-serif; overflow: hidden; }
  .layer { position: absolute; inset: 0; }

  /* Vorderseite */
  .page--front { background: var(--white); color: var(--ink); }
  .club-mark { position: absolute; display: flex; align-items: center; gap: 14px; }
  .club-mark__dot { width: 34px; height: 34px; border-radius: 50%; background: var(--green); flex: none; }
  .club-mark__name { font-weight: 800; font-size: 24px; line-height: 1.15; text-transform: uppercase; }
  .page--front .club-mark { left: 80px; top: 150px; width: 290px; }
  .page--front .club-mark__name { color: var(--black); }
  .headline { position: absolute; left: 64px; top: 452px; font-family: "Oswald", sans-serif; font-weight: 600; font-size: 66px; line-height: 76px; color: var(--white); letter-spacing: -0.5px; }
  .tagline { position: absolute; left: 66px; top: 622px; font-weight: 600; font-size: 23px; line-height: 27px; color: var(--white); }
  .thumb { position: absolute; top: 634px; height: 156px; }
  .thumb--one { left: 408px; width: 216px; background: linear-gradient(180deg, #c9d4c4 0%, #5c8f3e 45%, #3f7d2e 100%); }
  .thumb--two { left: 635px; width: 214px; background: linear-gradient(180deg, #7fae6d 0%, #4d8e35 50%, #3c7a2a 100%); }
  .info-box { position: absolute; left: 39px; top: 815px; width: 813px; height: 286px; border: 3px solid var(--green); display: flex; padding: 24px 34px 20px; }
  .info-box__col--about { width: 340px; padding-right: 26px; border-right: 2px solid var(--green); }
  .info-box__col--benefits { flex: 1; padding-left: 26px; }
  .info-box__title { font-weight: 800; font-size: 31px; line-height: 35px; color: var(--green); text-transform: uppercase; padding-bottom: 8px; border-bottom: 2px solid var(--green); margin-bottom: 18px; }
  .info-box__subtitle { font-weight: 700; font-size: 19px; line-height: 23px; color: var(--green); margin-bottom: 14px; }
  .info-box p { font-size: 13px; line-height: 16px; }
  .info-box p + p { margin-top: 16px; }
  .site-url { position: absolute; left: 0; right: 0; top: 1132px; padding-left: 20px; text-align: center; font-weight: 700; font-size: 24px; color: var(--green); }

  /* Rückseite */
  .page--back { background: var(--green); color: var(--white); }
  .back-block { position: absolute; }
  .back-block__title { font-weight: 700; font-size: 24px; line-height: 29px; text-transform: uppercase; padding-bottom: 10px; border-bottom: 2px solid var(--white); margin-bottom: 12px; }
  .back-block p { font-size: 14px; line-height: 16px; }
  .back-block--membership { left: 72px; top: 60px; width: 366px; }
  .back-block--donation { left: 475px; top: 43px; width: 376px; height: 158px; border: 3px solid var(--white); padding: 28px 26px 0; }
  .back-block--benefits { left: 44px; top: 250px; width: 387px; height: 420px; border: 3px solid var(--white); padding: 22px 28px 0; }
  .back-block--uses { left: 506px; top: 232px; width: 330px; }
  .back-photo { position: absolute; inset: 0; }
  .page--back .club-mark { left: 80px; top: 780px; width: 300px; }
  .page--back .club-mark__dot { background: var(--white); }
  .page--back .club-mark__name { color: var(--white); }
  .contact { position: absolute; left: 78px; top: 1078px; list-style: none; }
  .contact__item { display: flex; align-items: center; gap: 10px; font-weight: 600; font-size: 28px; line-height: 40px; color: var(--white); }
  .contact__icon { width: 24px; height: 24px; flex: none; }
</style>
</head>
<body>
<div class="canvas">

  <div class="page-slot page-slot--front">
    <main class="page page--front">
      <svg class="layer" width="889" height="1200" viewBox="0 0 889 1200" aria-hidden="true">
        <polygon points="0,385 419,332 656,583 889,524 889,623 419,636 140,782 0,723" fill="var(--green)"/>
        <polygon points="600,1200 889,1108 889,1200" fill="var(--black)"/>
      </svg>
      <svg class="layer" role="img" aria-label="Foto: jubelnde Jugendspieler in gelben Trikots umarmen sich im Stadion" width="889" height="1200" viewBox="0 0 889 1200">
        <defs>
          <linearGradient id="heroTone" x1="0" y1="0" x2="1" y2="1">
            <stop offset="0" stop-color="#7aa06a"/>
            <stop offset="0.45" stop-color="#e4d23a"/>
            <stop offset="1" stop-color="#2d3a6b"/>
          </linearGradient>
        </defs>
        <polygon points="342,0 889,0 889,518 656,583" fill="url(#heroTone)"/>
      </svg>

      <div class="club-mark">
        <span class="club-mark__dot"></span>
        <span class="club-mark__name">Fußball Förderverein Halmbeck e.V.</span>
      </div>

      <h1 class="headline">Unterstütze den<br>SpVg Halmbeck</h1>
      <p class="tagline">Gemeinsam für die<br>Zukunft unseres Vereins<br>und der Jugend!</p>

      <div class="thumb thumb--one" role="img" aria-label="Foto: Kinder beim Fußballspiel auf dem Rasen"></div>
      <div class="thumb thumb--two" role="img" aria-label="Foto: Training mit Ball und Hütchen"></div>

      <section class="info-box">
        <div class="info-box__col--about">
          <h2 class="info-box__title">Über den<br>Förderverein:</h2>
          <p>Lorem ipsum dolor sit amet, consectetur adipiscing elit, sed do eiusmod tempor incididunt ut labore et dolore magna aliqua. Ut enim ad minim veniam, quis nostrud exercitation ullamco laboris nisi ut aliquip ex ea commodo consequat. Duis aute irure dolor in reprehenderit in voluptate velit esse cillum dolore eu fugiat nulla pariatur.</p>
        </div>
        <div class="info-box__col--benefits">
          <h3 class="info-box__subtitle">Vorteile für Vereine und<br>Jugendliche:</h3>
          <p>Lorem ipsum dolor sit amet, consectetur adipiscing elit, sed do eiusmod tempor incididunt ut labore et dolore magna aliqua. Ut enim ad minim veniam, quis nostrud exercitation ullamco laboris nisi ut aliquip ex ea commodo consequat.</p>
          <p>Lorem ipsum dolor sit amet, consectetur adipiscing elit, sed do eiusmod tempor incididunt ut labore et dolore magna aliqua. Ut enim ad minim veniam, quis nostrud exercitation ullamco laboris nisi ut aliquip ex ea commodo consequat.</p>
        </div>
      </section>

      <p class="site-url">www.spvg-halmbeck.de</p>
    </main>
  </div>

  <div class="page-slot page-slot--back">
    <section class="page page--back">
      <div class="back-block back-block--membership">
        <h2 class="back-block__title">Mitgliedschaft:</h2>
        <p>Lorem ipsum dolor sit amet, consectetur adipiscing elit, sed do eiusmod tempor incididunt ut labore et dolore magna aliqua. Ut enim ad minim veniam, quis nostrud exercitation ullamco laboris nisi ut aliquip ex ea commodo consequat. Duis aute irure dolor in reprehenderit in voluptate velit esse cillum dolore eu fugiat nulla pariatur.</p>
      </div>

      <div class="back-block back-block--donation">
        <h2 class="back-block__title">Spenden:</h2>
        <p>Möglichkeit der direkten Spende mit einem Hinweis auf steuerliche Vorteile (falls zutreffend). Möglicherweise auch die Angabe eines Spendenkontos.</p>
      </div>

      <div class="back-block back-block--uses">
        <h2 class="back-block__title">Beispiele für die<br>Verwendung von<br>Mitteln:</h2>
        <p>Welche Projekte oder Anschaffungen wurden durch den Förderverein unterstützt (z.B. Trainingsmaterialien, Ausrüstung, Turniere, Jugendfahrten)?</p>
      </div>

      <div class="back-block back-block--benefits">
        <h2 class="back-block__title">Vorteile und der<br>Beitrag, der<br>benötigt wird.</h2>
        <p>Lorem ipsum dolor sit amet, consectetur adipiscing elit, sed do eiusmod tempor incididunt ut labore et dolore magna aliqua. Ut enim ad minim veniam, quis nostrud exercitation ullamco laboris nisi ut aliquip ex ea commodo consequat. Duis aute irure dolor in reprehenderit in voluptate velit esse cillum dolore eu fugiat nulla pariatur. Excepteur sint occaecat cupidatat non proident, sunt in culpa qui officia deserunt mollit anim id est laborum.</p>
      </div>

      <svg class="back-photo" role="img" aria-label="Foto: Fußballspieler in schwarzem Trikot im Stadion auf dem Rasen" width="889" height="1200" viewBox="0 0 889 1200">
        <defs>
          <linearGradient id="stadiumTone" x1="0" y1="0" x2="0" y2="1">
            <stop offset="0" stop-color="#9cc7e8"/>
            <stop offset="0.35" stop-color="#6f8a8c"/>
            <stop offset="0.55" stop-color="#3f7f3a"/>
            <stop offset="1" stop-color="#2f7a25"/>
          </linearGradient>
        </defs>
        <polygon points="0,712 889,446 889,462 0,729" fill="var(--white)"/>
        <polygon points="0,729 889,462 889,1039 733,1200 0,1200" fill="url(#stadiumTone)"/>
        <polygon points="733,1200 889,1039 889,1200" fill="var(--white)"/>
      </svg>

      <div class="club-mark">
        <span class="club-mark__dot"></span>
        <span class="club-mark__name">Fußball Förderverein Halmbeck e.V.</span>
      </div>

      <ul class="contact">
        <li class="contact__item">
          <svg class="contact__icon" viewBox="0 0 24 24" aria-hidden="true"><circle cx="12" cy="12" r="12" fill="var(--white)"/><path d="M8 6.5l2 0 1 3-1.4 1a7 7 0 0 0 3.9 3.9l1-1.4 3 1v2a1.5 1.5 0 0 1-1.6 1.5A10 10 0 0 1 6.5 8.1 1.5 1.5 0 0 1 8 6.5z" fill="var(--green-dark)"/></svg>
          123-456-7890
        </li>
        <li class="contact__item">
          <svg class="contact__icon" viewBox="0 0 24 24" aria-hidden="true"><circle cx="12" cy="12" r="12" fill="var(--white)"/><rect x="6" y="8" width="12" height="8.5" rx="1" fill="none" stroke="var(--green-dark)" stroke-width="1.6"/><path d="M6.5 8.7l5.5 4.2 5.5-4.2" fill="none" stroke="var(--green-dark)" stroke-width="1.6"/></svg>
          info@spvg-halmbeck.de
        </li>
        <li class="contact__item">
          <svg class="contact__icon" viewBox="0 0 24 24" aria-hidden="true"><circle cx="12" cy="12" r="12" fill="var(--white)"/><g fill="none" stroke="var(--green-dark)" stroke-width="1.4"><circle cx="12" cy="12" r="6"/><ellipse cx="12" cy="12" rx="2.6" ry="6"/><path d="M6 12h12"/></g></svg>
          spvg-halmbeck.de
        </li>
      </ul>
    </section>
  </div>

</div>
</body>
</html>
```